landscape and garden design business card

I would like a business card designed for my landscape and garden design company, Thistlecove Gardens. We are located in Colorado. I would like to include our logo, contact info, and social media/web site address or QR code. Looking for an organic, flowing design that incorporates our logo.

Target Market(s)

Homeowners and businesses that need garden and landscape design

Contact Information for Business Card

Would like it to say landscape and garden design

Requirements
Must have
• Landscape and garden design

```html
<!DOCTYPE html>
<html lang="en">
<head>
<meta charset="utf-8">
<title>Thistlecove Gardens – Business Card</title>
<link href="https://fonts.googleapis.com/css2?family=Poppins:wght@400;500;600&display=swap" rel="stylesheet">
<style>
  :root {
    --stage: #1d2021;
    --forest: #243432;
    --sage: #b4b5aa;
    --paper: #ffffff;
    --ink-light: #c9cac0;
  }
  * { margin: 0; padding: 0; box-sizing: border-box; }
  html, body { width: 1200px; height: 900px; overflow: hidden; }
  body {
    background: var(--stage);
    font-family: "Poppins", sans-serif;
    position: relative;
  }
  .card {
    position: absolute;
    left: 250px;
    width: 700px;
    height: 400px;
    overflow: hidden;
  }
  .card--back { top: 30px; background: var(--forest); }
  .card--front { top: 470px; background: var(--paper); }

  .brand {
    position: absolute;
    display: flex;
    flex-direction: column;
    align-items: center;
    width: 340px;
  }
  .brand__disc {
    width: 140px;
    height: 140px;
    border-radius: 50%;
  }
  .brand__name {
    margin-top: 12px;
    font-weight: 500;
    font-size: 34px;
    line-height: 1.05;
    text-align: center;
  }
  .brand__tagline {
    margin-top: 8px;
    font-weight: 400;
    font-size: 14px;
    letter-spacing: 1px;
  }
  .card--back .brand { left: 180px; top: 45px; }
  .card--back .brand__disc { background: var(--sage); }
  .card--back .brand__name,
  .card--back .brand__tagline { color: var(--sage); }

  .social {
    position: absolute;
    left: 0; right: 0;
    top: 340px;
    display: flex;
    justify-content: center;
    gap: 26px;
  }
  .social__dot {
    width: 22px; height: 22px;
    border-radius: 50%;
    background: var(--sage);
  }

  .front-shape { position: absolute; inset: 0; }
  .card--front .brand { left: 25px; top: 60px; }
  .card--front .brand__disc { background: var(--forest); }
  .card--front .brand__name,
  .card--front .brand__tagline { color: var(--forest); }

  .contact {
    position: absolute;
    left: 440px;
    top: 100px;
    width: 235px;
    color: var(--ink-light);
  }
  .contact__name {
    font-weight: 600;
    font-size: 20px;
    letter-spacing: 1.5px;
    text-transform: uppercase;
  }
  .contact__role { font-size: 15px; margin-bottom: 16px; white-space: nowrap; }
  .contact__address { font-size: 15px; line-height: 1.45; margin-bottom: 14px; white-space: nowrap; }
  .contact__line {
    display: flex;
    align-items: center;
    gap: 10px;
    font-size: 15px;
    line-height: 1.65;
    white-space: nowrap;
  }
  .contact__line svg { width: 14px; height: 14px; flex: none; }
</style>
</head>
<body>

  <section class="card card--back">
    <div class="brand">
      <div class="brand__disc" role="img" aria-label="Brand emblem area"></div>
      <div class="brand__name">Thistlecove<br>Gardens</div>
      <div class="brand__tagline">Landscape and garden design</div>
    </div>
    <div class="social">
      <span class="social__dot"></span>
      <span class="social__dot"></span>
      <span class="social__dot"></span>
    </div>
  </section>

  <section class="card card--front">
    <svg class="front-shape" viewBox="0 0 700 400" width="700" height="400">
      <path d="M385 0 C290 100 290 300 405 400 L700 400 L700 0 Z" fill="var(--sage)"/>
      <path d="M428 0 C340 110 340 290 450 400 L700 400 L700 0 Z" fill="var(--forest)"/>
    </svg>
    <div class="brand">
      <div class="brand__disc" role="img" aria-label="Brand emblem area"></div>
      <div class="brand__name">Thistlecove<br>Gardens</div>
      <div class="brand__tagline">Landscape and garden design</div>
    </div>
    <div class="contact">
      <div class="contact__name">Daniel Marsh</div>
      <div class="contact__role">Development Manager Officer</div>
      <div class="contact__address">412 Aspen Ridge Road<br>Suite 210, Boulder, CO 80302</div>
      <div class="contact__line">
        <svg viewBox="0 0 16 16"><path d="M3 1 L6 1 L7 5 L5 6.5 C6 9 7 10 9.5 11 L11 9 L15 10 L15 13 C15 14 14 15 13 15 C6 15 1 10 1 3 C1 2 2 1 3 1 Z" fill="currentColor"/></svg>
        720-555-0148
      </div>
      <div class="contact__line">
        <svg viewBox="0 0 16 16"><rect x="1" y="3" width="14" height="10" rx="1" fill="currentColor"/><path d="M1.5 3.5 L8 9 L14.5 3.5" stroke="var(--forest)" stroke-width="1.3" fill="none"/></svg>
        daniel@thistlecove.com
      </div>
      <div class="contact__line">
        <svg viewBox="0 0 16 16" fill="none" stroke="currentColor" stroke-width="1.2"><circle cx="8" cy="8" r="6.5"/><ellipse cx="8" cy="8" rx="3" ry="6.5"/><path d="M1.5 8 H14.5"/></svg>
        thistlecove.com
      </div>
    </div>
  </section>

</body>
</html>
```